Business Card Design Project

Use our current logo. Clean design.

Industry/Entity Type

Business

Requirements
Must have
• Marisela DUBRANCQ
M. Law
Managing Partner

Alpenvorsa AG
Kornhalmweg 214
CH-3097 Liebefeld

M. +41 79 412 56 27
T. +41 31 928 44 10
F. +41 31 928 44 19

m.dubrancq@alpenvorsa-example.com
www.alpenvorsa-example.com

```html
<!DOCTYPE html>
<html lang="en">
<head>
<meta charset="utf-8">
<title>Alpenvorsa AG – Business Cards</title>
<link rel="stylesheet" href="https://fonts.googleapis.com/css2?family=Didact+Gothic&display=swap">
<style>
  :root {
    --bg-light: #f4f4f4;
    --bg-dark: #d9d9d9;
    --ink: #1a1a1a;
    --ink-soft: #3a3a3a;
    --rule: #6a6a6a;
    --card-white: #ffffff;
    --card-black: #0a0a0a;
    --card-grey-top: #ececec;
    --card-grey-bottom: #dcdcdc;
    --panel-grey: #bdbdbd;
    --panel-grey-dark: #a9a9a9;
  }
  * { box-sizing: border-box; margin: 0; padding: 0; }
  html, body {
    width: 1200px;
    height: 1000px;
    overflow: hidden;
  }
  body {
    background: radial-gradient(ellipse at 50% 35%, var(--bg-light) 0%, var(--bg-dark) 100%);
    font-family: "Didact Gothic", "Century Gothic", sans-serif;
    color: var(--ink);
    position: relative;
  }
  .card {
    position: absolute;
    width: 520px;
    height: 330px;
    box-shadow: 0 6px 18px rgba(0,0,0,0.22);
    overflow: hidden;
  }

  /* Split card: black brand side, white details side */
  .card--split {
    left: 610px;
    top: 140px;
    display: flex;
    background: var(--card-white);
  }
  .card--split .brand-side {
    width: 44%;
    background: var(--card-black);
    display: flex;
    align-items: center;
    justify-content: center;
  }
  .card--split .brand-name {
    color: var(--card-white);
    font-size: 26px;
    letter-spacing: 1px;
  }
  .card--split .details-side {
    flex: 1;
    padding: 34px 26px 0 26px;
  }

  /* Grey card: details top-left, brand panel bottom-right */
  .card--grey {
    left: 70px;
    top: 530px;
    background: linear-gradient(160deg, var(--card-grey-top) 0%, var(--card-grey-bottom) 100%);
  }
  .card--grey .details-side {
    position: absolute;
    left: 34px;
    top: 28px;
    width: 290px;
  }
  .card--grey .brand-panel {
    position: absolute;
    left: 290px;
    top: 160px;
    width: 240px;
    height: 170px;
  }
  .card--grey .brand-panel svg { position: absolute; inset: 0; }
  .card--grey .brand-name {
    position: absolute;
    left: 28px;
    top: 72px;
    color: var(--ink);
    font-size: 24px;
    letter-spacing: 1px;
  }

  /* Shared contact block */
  .person-name { font-size: 23px; line-height: 1.1; color: var(--ink); }
  .person-role { font-size: 14px; line-height: 1.35; color: var(--ink-soft); margin-left: 4px; }
  .divider { border: 0; border-top: 1px solid var(--rule); margin: 12px 0 14px; }
  .contact-block { font-size: 12px; line-height: 1.4; color: var(--ink-soft); letter-spacing: 0.4px; }
  .contact-block + .contact-block { margin-top: 12px; }
  .card--split .contact-block { margin-left: 4px; }
</style>
</head>
<body>

  <section class="card card--split" aria-label="Business card, split black and white side">
    <div class="brand-side">
      <span class="brand-name">ALPENVORSA</span>
    </div>
    <div class="details-side">
      <h1 class="person-name">Marisela DUBRANCQ</h1>
      <p class="person-role">M. Law<br>Managing Partner</p>
      <hr class="divider">
      <p class="contact-block">Alpenvorsa AG<br>Kornhalmweg 214<br>CH-3097 Liebefeld</p>
      <p class="contact-block">M. +41 79 412 56 27<br>T. +41 31 928 44 10<br>F. +41 31 928 44 19</p>
      <p class="contact-block">m.dubrancq@alpenvorsa-example.com<br>www.alpenvorsa-example.com</p>
    </div>
  </section>

  <section class="card card--grey" aria-label="Business card, grey version">
    <div class="details-side">
      <h2 class="person-name">Marisela DUBRANCQ</h2>
      <p class="person-role">M. Law<br>Managing Partner</p>
      <hr class="divider">
      <p class="contact-block">Alpenvorsa AG<br>Kornhalmweg 214<br>CH-3097 Liebefeld</p>
      <p class="contact-block">M. +41 79 412 56 27<br>T. +41 31 928 44 10<br>F. +41 31 928 44 19</p>
      <p class="contact-block">m.dubrancq@alpenvorsa-example.com<br>www.alpenvorsa-example.com</p>
    </div>
    <div class="brand-panel">
      <svg width="240" height="170" viewBox="0 0 240 170" aria-hidden="true">
        <defs>
          <linearGradient id="panelFill" x1="0" y1="0" x2="1" y2="1">
            <stop offset="0" stop-color="var(--panel-grey)"/>
            <stop offset="1" stop-color="var(--panel-grey-dark)"/>
          </linearGradient>
        </defs>
        <polygon points="18,8 240,0 240,170 0,170" fill="url(#panelFill)"/>
      </svg>
      <span class="brand-name">ALPENVORSA</span>
    </div>
  </section>

</body>
</html>
```